Veltaro Resident Safety and Security

Need a website for our company. Please see attached outlines and files
Main Page
Veltaro
Design – Install – Maintain
Supporting the Safety and Security needs of your Community
Best in Class Systems for the Safety and Security of your Residents and Staff
Your Trusted Advisor
Solutions
Systems tailored to the needs of your facility
Skilled Nursing Facilities
Long Term Care
CCRC’s
Assisted Living
Independent Living
Access Control
Maglocks
Keypads
Prox readers (key fob, card, etc.)
Wireless locks
Multi-Tennant
Perimeter doors
Resident Apartment doors
Nurse Call
Tone / Visual
Fixed Stations
Dome Lights
T/V+ Audio
Fixed Stations
Dome Lights
Audio communication
Wireless
Fixed Stations
Resident Pendants
Hybrid Systems
Wired and Wireless integrated for seamless notification and reporting.
CCTV
Surveillance systems to fit your security needs and your budget
Remote Access, Local or Cloud Storage
Good, Better, Best proposals
Wander management
Door Alarming
Detection of wandering resident
Remote alarming and alerts
Delay elopement to allow for redirection
Network Infrastructure
Modern infrastructure for modern systems
Conference and Telepresence
Professionally installed systems to allow for seamless clear communications between teams across infinite distances.
Our Team
Mark Dunleavy – President
Paula Hobart – Vice President of Customer Success
Colin Marsh – Account Executive
Industry Associations
Granite Harbor Guild
Massachusetts chapter of the National Guild of Care Facility Stewards
Contact Us
Phone (603) 555-0172
Email Info@Veltaro-example.com
Facilities we serve
Independent Senior Living
Assisted Living
Memory Care
CCRC (Continuing Care Retirement Community)
Skilled Nursing / Rehab
Multi-Tenant
Outpatient Surgical Centers
Endoscopy Clinics
Acute Care
Urgent Care
Commercial Properties of all types
General notes
Imagery should invoke high tech, safety, security and include healthcare themes. the circuit board shield is our logo and a ghosted image as back ground or some animation that brings in the logo or the circuit board should be incorporated.
Veltaro is a systems integration company specializing in low voltage solutions for healthcare facilities and senior living communities. The company aims to leverage its industry expertise, and innovative products to become the market leader in systems integration, focusing on enhancing safety and operational efficiency.
Vision and Mission: Veltaro’s vision is to revolutionize integrated systems within healthcare and commercial environments by delivering innovative, reliable, and tailored solutions that enhance operational efficiency and patient care. The company is committed to setting new standards for resident safety and customer satisfaction.
Company Summary: Founded by experienced industry professionals, Veltaro specializes in the design, installation, and maintenance of systems including Access Control, Nurse Call, Delayed Egress, network infrastructure, and overhead paging primarily for healthcare clients.
Products and Services: The company offers a comprehensive range of low voltage systems including Nurse Call (wired and wireless), Wander Management, Access Control, and wired/wireless network infrastructure tailored for senior living and healthcare facilities.
Mission Statement
Veltaro was founded to fill a specific need. Senor living communities and healthcare facilities of all kinds face unique challenges in regards to technology and systems integration. Veltaro is perfectly positioned with an experienced management team, skilled technicians, industry relationships with suppliers and facility management groups. We have built our reputation on excellent customer service and the highest standards of integrity. Veltaro’s vision is to revolutionize integrated systems within healthcare and commercial environments by delivering innovative, reliable, and tailored solutions that enhance operational efficiency and patient care. We are committed to setting new standards for resident safety and customer satisfaction in every project we undertake.

Target Market(s)

Senior living communities staff and management

Industry/Entity Type

Systems Intergration

Coding

Coded - Design and coding required

Font styles to use
Serif
Sans Serif

Colors
0054AA
0677BA
7BADD7
CADEEF
E8F1F8
0094D4
00A9DD
6FCCEA
C7EBF8
E9F6FB

Requirements
Must have
• unique eye catching design including circuit board (PCB) type design and our supplied logo files

```html
<!DOCTYPE html>
<html lang="en">
<head>
<meta charset="utf-8">
<title>Veltaro Resident Safety and Security</title>
<link href="https://fonts.googleapis.com/css2?family=Inter+Tight:wght@300;400;500;600;700;800&display=swap" rel="stylesheet">
<style>
:root{
  --blue:#0b55c9;
  --blue-deep:#0054AA;
  --cyan:#00A9DD;
  --cyan-bright:#0fa8ef;
  --navy:#0e1746;
  --navy-mid:#1b2f86;
  --ink:#111418;
  --muted:#5b6270;
  --pale:#eef4fb;
  --card-line:#e4ebf4;
  --white:#ffffff;
}
*{margin:0;padding:0;box-sizing:border-box}
html,body{width:1200px;height:3161px;overflow:hidden}
body{position:relative;font-family:"Inter Tight",Arial,sans-serif;color:var(--ink);background:var(--white)}
.abs{position:absolute}
a{color:inherit;text-decoration:none}
.btn{position:absolute;display:flex;align-items:center;justify-content:center;gap:10px;background:var(--cyan-bright);color:var(--white);font-weight:700;font-size:13px;border-radius:4px;letter-spacing:-.1px;z-index:3}
.btn svg{width:24px;height:8px}
.eyebrow{font-size:13px;font-weight:700;letter-spacing:.9px;text-transform:uppercase}

/* top bar */
.topbar{left:0;top:0;width:1200px;height:29px;background:var(--blue);color:var(--white);font-size:11.5px;font-weight:500;display:flex;justify-content:flex-end;align-items:center;padding-right:174px;gap:12px}

/* hero */
.hero{left:0;top:29px;width:1200px;height:781px;overflow:hidden;background:
  radial-gradient(ellipse 520px 420px at 880px 360px,#2a56c8 0%,rgba(40,80,200,.35) 45%,transparent 75%),
  linear-gradient(160deg,#1a2660 0%,#151f55 35%,#1f3590 70%,#2a4fd0 100%)}
.brand{display:flex;flex-direction:column;align-items:center;gap:8px;width:150px}
.brand .mark{width:80px;height:80px;border-radius:50%;background:var(--cyan-bright)}
.brand .name{font-size:26px;font-weight:500;color:var(--cyan-bright);letter-spacing:.5px}
.hero .brand{left:170px;top:24px}
.nav{left:408px;top:42px;display:flex;gap:20px;color:var(--white);font-size:13px;font-weight:600}
.hero-contact{left:885px;top:31px;width:141px;height:39px}
.hero-copy{left:170px;top:256px;color:var(--white);z-index:2}
.hero-copy .eyebrow{font-size:15px;letter-spacing:.5px}
.hero-copy h1{margin-top:12px;font-size:52px;font-weight:400;line-height:57px;letter-spacing:-1.6px;white-space:nowrap}
.hero-copy h1 b{font-weight:800}
.hero-copy p{margin-top:14px;font-size:14.5px;font-weight:500;letter-spacing:-.2px}
.hero-btn{left:170px;top:496px;width:262px;height:47px}
.hero-art{left:712px;top:143px;width:360px;height:466px;border-radius:40px 40px 180px 180px;z-index:1;
  background:radial-gradient(circle at 50% 40%,#7fc4ff 0%,#2e74e6 45%,#16296e 100%)}
.hero-edge{left:0;top:700px}

/* services */
.services{left:0;top:810px;width:1200px;height:448px;background:var(--pale)}
.section-title{position:absolute;left:0;width:1200px;text-align:center;font-size:42px;font-weight:400;line-height:45px;letter-spacing:-1.3px}
.section-title b{font-weight:800}
.services .section-title{top:21px}
.services .lede{position:absolute;top:120px;width:1200px;text-align:center;font-size:14.5px;color:var(--muted)}
.service-cards{left:170px;top:159px;display:flex;gap:22px}
.service-card{width:197px;height:156px;background:var(--white);border-radius:10px;display:flex;flex-direction:column;align-items:center;justify-content:flex-end;padding-bottom:27px;text-align:center;font-size:18px;font-weight:500;line-height:22px;position:relative}
.service-card svg{position:absolute;top:20px;left:50%;transform:translateX(-50%);width:62px;height:62px;fill:none;stroke:var(--cyan-bright);stroke-width:3.4;stroke-linecap:round;stroke-linejoin:round}
.services .btn{left:508px;top:347px;width:178px;height:47px}

/* about */
.about-photo{left:170px;top:1300px;width:457px;height:497px;
  clip-path:polygon(50% 0%,100% 14%,100% 48%,90% 72%,72% 90%,50% 100%,28% 90%,10% 72%,0% 48%,0% 14%);
  background:linear-gradient(135deg,#c9d6e4 0%,#8fb0d6 40%,#3e6fb0 75%,#25324a 100%)}
.about-copy{left:670px;top:1317px;width:362px}
.about-copy .eyebrow{color:var(--blue);font-size:12.5px;letter-spacing:.6px}
.about-copy h2{margin-top:4px;font-size:44px;font-weight:400;line-height:45px;letter-spacing:-1.4px;white-space:nowrap}
.about-copy h2 b{font-weight:800}
.about-copy p{margin-top:20px;font-size:15px;line-height:21px;color:var(--muted)}
.about .btn{left:671px;top:1736px;width:261px;height:47px}

/* team */
.team-band{left:0;top:1840px}
.team .section-title{top:1933px;color:var(--white)}
.team-cards{left:170px;top:2045px;display:flex;gap:23px}
.team-card{width:270px;height:370px;background:var(--white);border-radius:0 0 8px 8px;box-shadow:0 6px 14px rgba(20,40,80,.08);text-align:center}
.team-card .photo{height:246px}
.team-card h3{margin-top:14px;font-size:19px;font-weight:500}
.team-card .role{margin-top:10px;font-size:14.5px;color:var(--muted)}
.team-card .links{margin-top:15px;display:flex;justify-content:center;gap:10px}
.team-card .links span{width:31px;height:31px;border-radius:50%;background:#eaf3fc;display:flex;align-items:center;justify-content:center}
.team-card .links svg{width:14px;height:14px;fill:var(--cyan-bright)}
.team-card .links .plain i{width:10px;height:10px;border-radius:2px;background:var(--cyan-bright);display:block}

/* facilities */
.facilities-copy{left:170px;top:2467px;width:410px}
.facilities-copy .eyebrow{color:var(--blue);font-size:12.5px;letter-spacing:.6px}
.facilities-copy h2{margin-top:4px;font-size:43px;font-weight:400;line-height:45px;letter-spacing:-1.3px;white-space:nowrap}
.facilities-copy h2 b{font-weight:800}
.facilities-copy p{margin-top:16px;font-size:15px;line-height:21px;color:var(--muted)}
.facilities-copy p + p{margin-top:21px}
.facilities-divider{left:598px;top:2466px;width:1px;height:319px;background:var(--card-line)}
.facility-list{left:638px;top:2465px;width:388px;list-style:none}
.facility-list li{height:30px;display:flex;justify-content:space-between;align-items:center;font-size:15px;font-weight:500}
.facility-list li::after{content:"+";font-size:17px;font-weight:600}

/* footer */
.footer{left:0;top:2816px;width:1200px;height:307px;background:var(--pale);overflow:hidden}
.footer .brand{left:170px;top:92px}
.footer-col{top:96px}
.footer-col h4{font-size:17px;font-weight:600;letter-spacing:-.2px;margin-bottom:9px}
.footer-col a,.footer-col span{display:block;font-size:14.5px;line-height:22.5px;color:var(--muted)}
.footer-col h4.follow{margin-top:23px;margin-bottom:0}
.socials{display:flex;gap:8px;margin-top:15px}
.socials i{width:44px;height:44px;border-radius:50%;background:var(--white);box-shadow:0 2px 6px rgba(20,60,120,.08);display:flex;align-items:center;justify-content:center}
.socials i::before{content:"";width:12px;height:12px;border-radius:50%;background:var(--cyan-bright)}
.copyright{left:0;top:3123px;width:1200px;height:38px;background:var(--blue);color:var(--white);font-size:13px;display:flex;align-items:center;justify-content:center}
</style>
</head>
<body>

<div class="abs topbar"><span>Phone: (603) 555-0172</span><span>|</span><span>Email: Info@Veltaro-example.com</span></div>

<header class="abs hero" role="img" aria-label="Dark blue circuit board background with glowing data lines">
  <div class="abs brand"><span class="mark"></span><span class="name">Veltaro</span></div>
  <nav class="abs nav"><a>About</a><a>Our Services</a><a>Resources</a><a>Innovation</a><a>Careers</a></nav>
  <a class="btn hero-contact">Contact Us <svg viewBox="0 0 24 8"><path d="M0 4h22M18 1l4 3-4 3" stroke="#fff" fill="none" stroke-width="1.3"/></svg></a>
  <div class="abs hero-art" role="img" aria-label="Glowing glass security shield filled with binary code"></div>
  <div class="abs hero-copy">
    <div class="eyebrow">Design – Install – Maintain</div>
    <h1>Supporting The Safety<br>and <b>Security Needs Of</b><br>Your Community.</h1>
    <p>Best in Class Systems for the Safety and Security of your Residents and Staff</p>
  </div>
  <a class="btn hero-btn">Learn More About Our Purpose <svg viewBox="0 0 24 8"><path d="M0 4h22M18 1l4 3-4 3" stroke="#fff" fill="none" stroke-width="1.3"/></svg></a>
  <svg class="abs hero-edge" width="1200" height="110" viewBox="0 0 1200 110"><polygon points="600,110 1200,22 1200,110" fill="#0fa8ef"/></svg>
</header>

<section class="abs services">
  <h2 class="section-title">Systems Tailored To The Needs<br><b>Of Your Facility</b></h2>
  <p class="lede">Customized solution that seamlessly delivers facility services within your budget</p>
  <div class="abs service-cards">
    <div class="service-card"><svg viewBox="0 0 64 64"><rect x="8" y="18" width="48" height="36" rx="9"/><path d="M24 18v-6h16v6M32 28v16M24 36h16M14 26v20"/></svg>Nurse Call</div>
    <div class="service-card"><svg viewBox="0 0 64 64"><path d="M32 6L4 56h56z"/><path d="M32 24v16M32 47v1"/></svg>Wander<br>Management</div>
    <div class="service-card"><svg viewBox="0 0 64 64"><path d="M22 60V18a12 12 0 0 1 24 0v8M22 40h8M46 34v24"/><circle cx="34" cy="22" r="4"/></svg>Access Control</div>
    <div class="service-card"><svg viewBox="0 0 64 64"><circle cx="32" cy="32" r="7"/><circle cx="12" cy="10" r="5"/><circle cx="52" cy="10" r="5"/><circle cx="12" cy="54" r="5"/><circle cx="52" cy="54" r="5"/><circle cx="8" cy="32" r="4"/><path d="M16 14l11 13M48 14L37 27M16 50l11-13M48 50L37 37M12 32h13"/></svg>Wired/wireless<br>Network</div>
  </div>
  <a class="btn">View All Services <svg viewBox="0 0 24 8"><path d="M0 4h22M18 1l4 3-4 3" stroke="#fff" fill="none" stroke-width="1.3"/></svg></a>
</section>

<section class="about">
  <div class="abs about-photo" role="img" aria-label="Doctor and administrator reviewing a tablet, framed in a shield shape"></div>
  <div class="abs about-copy">
    <div class="eyebrow">Committed to setting new standards</div>
    <h2>Revolutionize<br>Integrated Systems<br>Within <b>Healthcare</b><br><b>and Commercial</b><br>Environments</h2>
    <p>Veltaro was founded to fill a specific need. Senor living communities and healthcare facilities of all kinds face unique challenges in regards to technology and systems integration. Veltaro is perfectly positioned with an experienced management team, skilled technicians, industry relationships with suppliers and facility management groups.</p>
  </div>
  <a class="btn">Get Our Strategic Growth Story <svg viewBox="0 0 24 8"><path d="M0 4h22M18 1l4 3-4 3" stroke="#fff" fill="none" stroke-width="1.3"/></svg></a>
</section>

<section class="team">
  <svg class="abs team-band" width="1200" height="452" viewBox="0 0 1200 452">
    <polygon points="0,0 1200,0 1200,452 0,452" fill="#0b55c9"/>
    <polygon points="0,0 1200,0 0,93" fill="#0fa8ef"/>
  </svg>
  <h2 class="section-title">Specialists Who Understand Your<br><b>Environment</b></h2>
  <div class="abs team-cards">
    <article class="team-card">
      <div class="photo" role="img" aria-label="Portrait of the company president in an office" style="background:linear-gradient(180deg,#5d6f82,#2d3a4c)"></div>
      <h3>Mark Dunleavy</h3><div class="role">President</div>
      <div class="links"><span><svg viewBox="0 0 24 24"><path d="M6.6 10.8a15 15 0 0 0 6.6 6.6l2.2-2.2a1 1 0 0 1 1-.25 11.4 11.4 0 0 0 3.6.57 1 1 0 0 1 1 1V20a1 1 0 0 1-1 1A17 17 0 0 1 3 4a1 1 0 0 1 1-1h3.5a1 1 0 0 1 1 1c0 1.25.2 2.45.57 3.6a1 1 0 0 1-.25 1z"/></svg></span><span><svg viewBox="0 0 24 24"><path d="M2 5h20v14H2z M2 6l10 7 10-7" stroke="#eaf3fc" stroke-width="1.6"/></svg></span><span class="plain"><i></i></span></div>
    </article>
    <article class="team-card">
      <div class="photo" role="img" aria-label="Portrait of the vice president of customer success" style="background:linear-gradient(180deg,#8a8e96,#b9c6d6)"></div>
      <h3>Paula Hobart</h3><div class="role">Vice President of Customer Success</div>
      <div class="links"><span><svg viewBox="0 0 24 24"><path d="M6.6 10.8a15 15 0 0 0 6.6 6.6l2.2-2.2a1 1 0 0 1 1-.25 11.4 11.4 0 0 0 3.6.57 1 1 0 0 1 1 1V20a1 1 0 0 1-1 1A17 17 0 0 1 3 4a1 1 0 0 1 1-1h3.5a1 1 0 0 1 1 1c0 1.25.2 2.45.57 3.6a1 1 0 0 1-.25 1z"/></svg></span><span><svg viewBox="0 0 24 24"><path d="M2 5h20v14H2z M2 6l10 7 10-7" stroke="#eaf3fc" stroke-width="1.6"/></svg></span><span class="plain"><i></i></span></div>
    </article>
    <article class="team-card">
      <div class="photo" role="img" aria-label="Portrait of the account executive in a bright office" style="background:linear-gradient(180deg,#dfe4ea,#7da3cf)"></div>
      <h3>Colin Marsh</h3><div class="role">Account Executive</div>
      <div class="links"><span><svg viewBox="0 0 24 24"><path d="M6.6 10.8a15 15 0 0 0 6.6 6.6l2.2-2.2a1 1 0 0 1 1-.25 11.4 11.4 0 0 0 3.6.57 1 1 0 0 1 1 1V20a1 1 0 0 1-1 1A17 17 0 0 1 3 4a1 1 0 0 1 1-1h3.5a1 1 0 0 1 1 1c0 1.25.2 2.45.57 3.6a1 1 0 0 1-.25 1z"/></svg></span><span><svg viewBox="0 0 24 24"><path d="M2 5h20v14H2z M2 6l10 7 10-7" stroke="#eaf3fc" stroke-width="1.6"/></svg></span><span class="plain"><i></i></span></div>
    </article>
  </div>
</section>

<section class="facilities">
  <div class="abs facilities-copy">
    <div class="eyebrow">Facilities we serve</div>
    <h2>Supporting the<br>Spaces That <b>Support</b><br><b>Others</b></h2>
    <p>The company aims to leverage its industry expertise, and innovative products to become the market leader in systems integration, focusing on enhancing safety and operational efficiency.</p>
    <p>The company is committed to setting new standards for resident safety and customer satisfaction.</p>
  </div>
  <div class="abs facilities-divider"></div>
  <ul class="abs facility-list">
    <li>Independent Senior Living</li>
    <li>Assisted Living</li>
    <li>Memory Care</li>
    <li>CCRC (Continuing Care Retirement Community)</li>
    <li>Skilled Nursing / Rehab</li>
    <li>Multi-Tenant</li>
    <li>Outpatient Surgical Centers</li>
    <li>Endoscopy Clinics</li>
    <li>Acute Care</li>
    <li>Urgent Care</li>
    <li>Commercial Properties of all types</li>
  </ul>
</section>

<footer class="abs footer">
  <svg class="abs" style="left:0;top:0" width="1200" height="100" viewBox="0 0 1200 100"><polygon points="632,55 1200,0 1200,92" fill="#0fa8ef"/></svg>
  <div class="abs brand"><span class="mark"></span><span class="name">Veltaro</span></div>
  <div class="abs footer-col" style="left:389px"><h4>Quick Links</h4><a>About</a><a>Services</a><a>Facilities We Serve</a><a>Innovation</a><a>Careers</a><a>Contact Us</a></div>
  <div class="abs footer-col" style="left:598px"><h4>Legal Info</h4><a>Client Pay</a><a>Terms and conditions</a><a>Privacy Policy</a><a>Project Bid Info</a><a>Refund Policy</a></div>
  <div class="abs footer-col" style="left:828px"><h4>Contact Us</h4><span>Phone: (603) 555-0172</span><span>Email: Info@Veltaro-example.com</span><h4 class="follow">Follow Us</h4>
    <div class="socials" aria-label="Social profiles"><i></i><i></i><i></i><i></i></div></div>
</footer>

<div class="abs copyright">Copyright © 2025 Veltaro. All Rights Reserved.</div>

</body>
</html>
```